Dentist logo, business card and website

I have done an amateur job of creating a logo, business card and website. I would like it to look more professional. the current website can be found at www.dorenkamsel.com - I would like the website to be built and run through wix.com. The content on the website is as I would like it but I am open to suggestions.

The logo should be simple, may be best to keep to the letter DK - maybe to look like the V is a reflection of the A? Again, I am open to suggestions (I have attached a couple of images I have used on presentations but I would like the logo that you design to have a 'no fill' background so it can be placed on slides (for presentations etc).

The colour scheme seems wrong for a dentist, perhaps duck egg with black writing would be better? This applies to the business card as well (I have attached a PDF of some I have had made in the past but again they look amateur and colour scheme is wrong. The business cards should be landscape, have the logo in the top right corner, my name and qualifications in the middle, and my website and physical address in the bottom left corner: Glanmorfa Dental Surgery, 41-43 Ffordd y Bont, Cardiff CF23 9RT.

Target Market(s)

30-60 year olds

Industry/Entity Type

Dental

Contact Information for Business Card

Please see brief and uploads.

Logo Text

DK

Number of Pages Required

4 page

Font styles to use
Decorative
Script

Requirements
Must have
• A sophisticated mature feel.
Nice to have
• Simplicity.
Should not have
• Anything too complicated.

```html
<!DOCTYPE html>
<html lang="en">
<head>
<meta charset="utf-8">
<title>Patient Testimonials – Doren Kamsel</title>
<link href="https://fonts.googleapis.com/css2?family=Lora:wght@400;500&display=swap" rel="stylesheet">
<style>
  :root{
    --ink:#0a0a0a;
    --paper:#ecebe6;
    --gold:#9a7c51;
    --white:#ffffff;
    --rule:#cfcdc6;
  }
  *{margin:0;padding:0;box-sizing:border-box}
  html,body{width:1200px;height:1000px;overflow:hidden}
  body{background:var(--ink);font-family:"Lora",Georgia,serif;color:var(--ink);position:relative}
  .top-band{position:absolute;left:0;top:0;width:1200px;height:54px;background:var(--ink)}
  .site-header{position:absolute;left:0;top:54px;width:1200px;height:112px;background:var(--paper);border-bottom:1px solid var(--rule)}
  .brand{position:absolute;left:0;width:1200px;top:70px;text-align:center;font-size:17px;color:var(--gold);letter-spacing:.2px}
  .main-nav{position:absolute;left:0;top:166px;width:1200px;height:25px;background:var(--ink);display:flex;justify-content:center;align-items:center;gap:26px}
  .main-nav a{color:var(--white);text-decoration:none;font-size:11.5px}
  .main-nav a.is-current{color:var(--gold)}
  .content{position:absolute;left:0;top:191px;width:1200px;height:623px;background:var(--paper)}
  .page-title{position:absolute;left:0;width:1200px;top:24px;text-align:center;font-size:22px;font-weight:400;color:var(--gold)}
  .testimonial{position:absolute;left:246px;width:705px}
  .testimonial p{font-size:11.2px;line-height:15px;text-align:justify}
  .testimonial p + p{margin-top:15px}
  .testimonial .author{text-align:right;margin-top:5px}
  .author-name{display:block;font-size:17px;line-height:20px;color:var(--gold)}
  .author-place{display:block;font-size:11.2px;line-height:14px}
  .submit-btn{position:absolute;left:549px;top:586px;width:102px;height:13px;border-radius:7px;background:var(--gold);color:var(--white);font-size:7.5px;line-height:13px;text-align:center;text-decoration:none}
  .site-footer{position:absolute;left:0;top:815px;width:1200px;height:185px;background:var(--ink);color:var(--white)}
  .footer-brand{position:absolute;left:246px;top:78px;font-size:15px;color:var(--gold)}
  .footer-col{position:absolute;top:25px;font-size:7.6px;line-height:10.5px}
  .footer-col h3{font-size:10px;font-weight:400;color:var(--gold);letter-spacing:.3px;margin-bottom:8px;text-transform:uppercase}
  .contact{left:515px}
  .contact .phone{margin-top:10.5px}
  .hours{left:803px;width:152px}
  .hours table{border-collapse:collapse;width:100%}
  .hours td{padding:0;line-height:10.5px}
  .hours td.time{padding-left:40px;white-space:nowrap}
</style>
</head>
<body>
  <div class="top-band"></div>
  <header class="site-header">
    <div class="brand">Doren Kamsel</div>
  </header>
  <nav class="main-nav">
    <a href="#">Home</a>
    <a href="#">About Me</a>
    <a href="#" class="is-current">Testimonials</a>
    <a href="#">Patient Resources</a>
    <a href="#">Contact</a>
  </nav>
  <main class="content">
    <h1 class="page-title">Patient Testimonials</h1>

    <article class="testimonial" style="top:67px">
      <p>Dr Doren Kamsel has been my dentist for several years now, I can quite confidently say that he is one of the most outstanding professionals I have encountered, not just in the medical world, but in all walks of life. As an international opera singer, my teeth are very important to me, both their appearance and function, and Doren’s brilliance and skill in their care is a source of great reassurance. In addition to his professional virtuosity, Doren is an exceptional person, endlessly kind, witty and interested in his patients. I am proud to give him my highest possible recommendation.</p>
      <div class="author"><span class="author-name">Edmund</span><span class="author-place">London</span></div>
    </article>

    <article class="testimonial" style="top:237px">
      <p>Doren firstly is a lovely guy, that’s the first thing that strikes you, it’s not often you get treated in such a nice manner at a dentist!</p>
      <p>I am someone that has always feared the dentist for years and years and hadn’t even stepped foot in a dentist for over 5 years. From the first discussion with Doren, he fully put me at ease and dispelled my fears. Doren has transformed my view of going to the dentist and also educated me along the way as to how to prevent issues in the future.</p>
      <p>Doren has performed a number of procedures on me including an extraction and root canal and safe to say I couldn’t have been treated with any more care and it made the experience as painless as possible.</p>
      <p>All in all, Doren has been a huge factor in removing my long time fear of the dentist and I enjoy my visits now and know I will be greeted with a warm welcome from someone who cares about my wellbeing.</p>
      <div class="author"><span class="author-name">Gareth</span><span class="author-place">Cardiff</span></div>
    </article>

    <article class="testimonial" style="top:496px">
      <p>…Throughout the treatment Doren could not have been more attentive..Every step and option was clearly explained to me in a reassuring and understandable way to enable me to make informed decisions about my treatment…</p>
      <div class="author"><span class="author-name">Morgan</span><span class="author-place">Roath, Cardiff</span></div>
    </article>

    <a href="#" class="submit-btn">Submit your testimonial</a>
  </main>

  <footer class="site-footer">
    <div class="footer-brand">Doren Kamsel</div>
    <div class="footer-col contact">
      <h3>Get in touch</h3>
      <div>Glanmorfa Dental Surgery</div>
      <div>41-43 Ffordd y Bont</div>
      <div>Cardiff</div>
      <div>CF23 9RT</div>
      <div class="phone">029 2048 3170</div>
    </div>
    <div class="footer-col hours">
      <h3>Glanmorfa opening times</h3>
      <table>
        <tr><td>Monday</td><td class="time">8.00am - 8.00pm</td></tr>
        <tr><td>Tuesday</td><td class="time">8.00am - 8.00pm</td></tr>
        <tr><td>Wednesday</td><td class="time">8.00am - 8.00pm</td></tr>
        <tr><td>Thursday</td><td class="time">8.00am - 8.00pm</td></tr>
        <tr><td>Friday</td><td class="time">8.00am - 5.30pm</td></tr>
        <tr><td>Saturday</td><td class="time">8.15am &nbsp;- 4.30pm</td></tr>
      </table>
    </div>
  </footer>
</body>
</html>
```